Redesign of Real Estate Agency Website

We need a redesign for our real estate agency website. Please see attached creative brief.

Target Market(s)

Refer to creative brief.

Industry/Entity Type

Real Estate

Requirements
Must have
• Refer to creative brief.

```html
<!DOCTYPE html>
<html lang="en">
<head>
<meta charset="utf-8">
<title>Islandnest – Property and Real Estate</title>
<link href="https://fonts.googleapis.com/css2?family=PT+Sans:wght@400;700&family=Open+Sans:wght@400;600;700&display=swap" rel="stylesheet">
<style>
:root{
  --page:#eef5f9;
  --topbar:#e6f0f5;
  --link:#1691d4;
  --ink:#2b3a44;
  --muted:#555f66;
  --line:#d7e2e8;
  --panel:#ffffff;
  --search:#a9daf3;
  --search-edge:#8cc8e8;
  --accent:#f9a11b;
  --accent-dark:#ef8a0c;
  --price:#f4a11d;
  --nav-active:#1b9ad9;
  --hot:#c62828;
}
*{box-sizing:border-box;margin:0;padding:0}
html,body{width:1200px;height:900px;overflow:hidden}
body{background:linear-gradient(#f3f8fb,var(--page));font-family:"Open Sans",Tahoma,sans-serif;color:var(--ink);position:relative}
a{color:var(--link);text-decoration:none}
.abs{position:absolute}
.topbar{left:0;top:0;width:1200px;height:28px;background:var(--topbar);border-bottom:1px solid #dbe7ee}
.toplinks{right:110px;top:6px;display:flex;gap:16px;font:700 12px "Open Sans",sans-serif}
.toplinks a{display:flex;align-items:center;gap:5px}
.toplinks i{display:inline-block;width:10px;height:10px;border-radius:2px}
.brand{left:110px;top:56px;display:flex;align-items:center;gap:10px}
.brand-mark{width:52px;height:52px;background:var(--link);border-radius:4px}
.brand-name{font:700 30px "PT Sans",sans-serif;color:#4a5560;line-height:1}
.brand-tag{font:700 10px "PT Sans",sans-serif;color:#7a858c;letter-spacing:.3px;margin-top:3px}
.cart{left:862px;top:57px;width:228px;height:38px;background:#fff;border:1px solid var(--line);border-radius:3px;padding:4px 0 0 40px;font-size:11px;line-height:13px;color:var(--muted)}
.cart a{font-weight:700}
.cart svg{position:absolute;left:7px;top:6px}
.nav{left:110px;top:128px;display:flex;height:33px;font:700 15px "PT Sans",sans-serif}
.nav a{color:var(--ink);padding:0 10px;line-height:33px;margin-right:0}
.nav a:first-child{padding-left:15px}
.nav .active{background:linear-gradient(#3fb3ea,var(--nav-active));color:#fff;border-radius:3px;position:relative}
.nav .active:after{content:"";position:absolute;left:50%;bottom:-6px;margin-left:-6px;border:6px solid transparent;border-bottom:0;border-top-color:var(--nav-active)}
.panel{background:var(--panel);border:1px solid var(--line);border-radius:2px}
.hero{left:110px;top:171px;width:980px;height:361px}
.search{left:126px;top:187px;width:324px;height:329px;background:linear-gradient(#b6e0f6,var(--search));border:1px solid var(--search-edge);border-radius:2px;overflow:hidden}
.search h2{position:absolute;left:15px;top:12px;font:700 15px "PT Sans",sans-serif;color:#2d4553}
.search .ring{position:absolute;right:-40px;top:-10px;width:150px;height:150px;border:22px solid rgba(255,255,255,.2);border-radius:50%}
.select{position:absolute;left:16px;width:292px;height:30px;background:#fff;border:1px solid #c9dde8;border-radius:2px;font-size:12.5px;color:#333;padding:6px 0 0 9px}
.select:after{content:"";position:absolute;right:9px;top:12px;border:5px solid transparent;border-bottom:0;border-top-color:#9aa6ad}
.more{position:absolute;left:18px;top:285px;font-size:11.5px;line-height:13px;color:#333}
.more a{font-weight:700}
.btn{position:absolute;left:171px;top:283px;width:137px;height:29px;background:linear-gradient(#fdb73a,var(--accent-dark));border-radius:2px;color:#fff;font:700 12px "Open Sans",sans-serif;padding:6px 0 0 10px}
.btn svg{position:absolute;right:8px;top:7px}
.slide{left:465px;top:187px;width:609px;height:329px;border-radius:3px;overflow:hidden;background:linear-gradient(180deg,#9fb8c8 0%,#b9c9cf 30%,#7d8a70 48%,#e9e4da 62%,#cfc6b7 100%)}
.slide-cap{position:absolute;left:0;top:0;width:100%;height:40px;background:rgba(40,40,40,.65);color:#fff;font-size:15px;padding:10px 0 0 15px}
.slide-cap b{font-weight:700}
.dots{position:absolute;right:16px;bottom:16px;display:flex;gap:3px}
.dots span{width:16px;height:16px;background:#333;color:#fff;font:700 10px/16px "Open Sans",sans-serif;text-align:center;border-radius:2px}
.dots .on{background:var(--nav-active)}
.latest{left:110px;top:547px;width:980px;height:231px}
.section-title{position:absolute;font:700 15px "PT Sans",sans-serif;color:#2d3a42}
.more-link{position:absolute;font:700 12.5px "Open Sans",sans-serif}
.arrow{position:absolute;top:95px;font:400 44px "PT Sans",sans-serif;color:#a7d3ec}
.card{position:absolute;top:43px;width:148px}
.thumb{width:138px;height:97px;border:1px solid #cfdde5;padding:3px;background:#fff;position:relative;overflow:hidden}
.thumb div{width:100%;height:100%}
.ribbon{position:absolute;left:-18px;top:13px;width:90px;height:14px;background:var(--hot);color:#fff;font:700 8px/14px "Open Sans",sans-serif;text-align:center;transform:rotate(-35deg)}
.card h3{margin:8px 0 0 3px;font:700 12.5px/14px "Open Sans",sans-serif;color:var(--link);width:138px}
.card p{margin-left:3px;font-size:11px;line-height:13px;color:#333}
.card .price{font-weight:700;color:var(--price);font-size:12.5px;line-height:15px}
.browse{left:110px;top:793px;width:265px;height:120px}
.browse ul{position:absolute;left:14px;top:36px;list-style:none;font-size:13px;line-height:20px}
.browse li:before{content:"›";color:#999;margin-right:4px}
.browse a{font-weight:700}
.hot{left:390px;top:793px;width:558px;height:120px;background:#faf8f5}
.hot-head{position:absolute;left:0;top:0;width:100%;height:42px;border-bottom:1px solid var(--line)}
.hot-photo{position:absolute;left:15px;top:58px;width:245px;height:80px;border:1px solid #ddd;background:linear-gradient(#9fb0bd,#6c6f70)}
.hot-info{position:absolute;left:270px;top:55px;font-size:11.5px;line-height:14px;color:#222}
.hot-info h3{font:700 13px "Open Sans",sans-serif;color:var(--link);margin-bottom:3px}
.hot-info dl{display:grid;grid-template-columns:143px 140px}
.hot-info b{font-weight:700}
.hot-info .p b,.hot-info .p{color:var(--price)}
.badge{left:964px;top:793px;width:126px;height:120px}
.badge div{position:absolute;left:15px;top:15px;width:94px;height:110px;background:#111;border-top:6px solid #b01d24}
</style>
</head>
<body>
<div class="abs topbar"></div>
<nav class="abs toplinks">
  <a href="#"><i style="background:#3b5a98"></i>Social connect</a>
  <a href="#"><i style="background:#f0b400"></i>Login</a>
  <a href="#"><i style="background:#f08a16"></i>RSS Feed</a>
</nav>

<div class="abs brand">
  <div class="brand-mark"></div>
  <div>
    <div class="brand-name">Islandnest</div>
    <div class="brand-tag">PROPERTY AND REAL ESTATE</div>
  </div>
</div>

<div class="abs cart">
  <svg width="26" height="24" viewBox="0 0 26 24"><path d="M1 3h4l3 12h13l3-9H7" fill="none" stroke="#9aa4aa" stroke-width="2"/><circle cx="10" cy="20" r="2" fill="#9aa4aa"/><circle cx="19" cy="20" r="2" fill="#9aa4aa"/></svg>
  2 items in <a href="#">sales inquiry cart</a><br>0 items in <a href="#">rentals inquiry cart</a>
</div>

<nav class="abs nav">
  <a href="#">HOME</a>
  <a href="#" class="active">PROPRETY FOR SALE</a>
  <a href="#">PROPRETY FOR RENT</a>
  <a href="#">ABOUT US</a>
  <a href="#">LIST YOUR PROPRETY</a>
  <a href="#">PROPRETY BUYER'S GUIDE</a>
  <a href="#">CONTACT US</a>
</nav>

<div class="abs panel hero"></div>
<form class="abs search">
  <div class="ring"></div>
  <h2>Quick Property Search</h2>
  <div class="select" style="top:42px">Buy proprety</div>
  <div class="select" style="top:82px">Proprety type</div>
  <div class="select" style="top:122px">Region</div>
  <div class="select" style="top:162px">District</div>
  <div class="select" style="top:202px">Minimum bedrooms</div>
  <div class="select" style="top:242px">Maximum price (THB)</div>
  <div class="more">Need more options?<br><a href="#">Advanced search »</a></div>
  <div class="btn">Proprety search<svg width="15" height="15" viewBox="0 0 15 15"><circle cx="7.5" cy="7.5" r="7" fill="#fff"/><path d="M4 7.5h6M7.5 4.5l3 3-3 3" stroke="#f08a0c" stroke-width="1.8" fill="none"/></svg></div>
</form>

<div class="abs slide" role="img" aria-label="Terrace with wicker chairs overlooking a tropical bay with islands">
  <div class="slide-cap"><b>Propreties of the month:</b> Affordable Modern 2 Bedroom Houses for SALE</div>
  <div class="dots"><span>1</span><span>2</span><span class="on">3</span><span>4</span></div>
</div>

<section class="abs panel latest">
  <h2 class="section-title" style="left:16px;top:14px">Latest Propreties Added</h2>
  <a class="more-link" href="#" style="right:15px;top:14px">View all new additions »</a>
  <span class="arrow" style="left:14px">«</span>
  <span class="arrow" style="right:14px">»</span>

  <div class="card" style="left:50px">
    <div class="thumb"><div role="img" aria-label="Villa garden lit at night" style="background:linear-gradient(#1d2a1e,#4d6a2c)"></div></div>
    <h3>The Palm Grove Estate PH.2</h3><p>Layan, North Phuket<br>Villa</p><p class="price">THB 16.9M - 17.7M</p>
  </div>
  <div class="card" style="left:198px">
    <div class="thumb"><div role="img" aria-label="Villa with pool at dusk" style="background:linear-gradient(#2b4fa8,#d08a3c 60%,#2a9bd0)"></div><span class="ribbon">HOT DEAL</span></div>
    <h3>Coral Bay Grand Villa Luxury</h3><p>Nai Harn, South Phuket<br>Villa</p><p class="price">THB 16.9M - 17.7M</p>
  </div>
  <div class="card" style="left:346px">
    <div class="thumb"><div role="img" aria-label="Penthouse bedroom interior" style="background:linear-gradient(#8a5a2e,#c89a6a 60%,#5b3218)"></div></div>
    <h3>3-bed Foreign Freehold Pentho…</h3><p>Kata, West Phuket<br>Apartment/Condo</p><p class="price">THB 16.9M - 17.7M</p>
  </div>
  <div class="card" style="left:494px">
    <div class="thumb"><div role="img" aria-label="Residence building against blue sky" style="background:linear-gradient(#8fc0e6,#e4ecef 55%,#9fb59a)"></div><span class="ribbon">HOT DEAL</span></div>
    <h3>Sunridge Hill Residence</h3><p>Karon, West Phuket<br>Apartment/Condo</p><p class="price">THB 16.9M - 17.7M</p>
  </div>
  <div class="card" style="left:642px">
    <div class="thumb"><div role="img" aria-label="Sea view through glass doors" style="background:linear-gradient(90deg,#2b2b2b,#9fc6de 20%,#6aa6cc 80%,#2b2b2b)"></div></div>
    <h3>Amaris Villa</h3><p style="margin-top:14px">Patong, West Phuket<br>Villa</p><p class="price">THB 16.9M - 17.7M</p>
  </div>
  <div class="card" style="left:790px">
    <div class="thumb"><div role="img" aria-label="Thai style pool villa" style="background:linear-gradient(#6fb0e0,#c0522a 55%,#4fa7c9)"></div></div>
    <h3>4 Bedroom Naiharn Pool Villa</h3><p>Nai Harn, South Phuket<br>Villa</p><p class="price">THB 16.9M - 17.7M</p>
  </div>
</section>

<section class="abs panel browse">
  <h2 class="section-title" style="left:14px;top:11px">Browse Property for Sale</h2>
  <ul>
    <li><a href="#">Hot Properties &amp; Promotions</a> (21)</li>
    <li><a href="#">Apartments &amp; Condos</a> (55)</li>
    <li><a href="#">Villas &amp; Houses</a> (76)</li>
    <li><a href="#">Land</a> (12)</li>
  </ul>
</section>

<section class="abs panel hot">
  <div class="hot-head">
    <h2 class="section-title" style="left:14px;top:11px">Hot Villas for Sale</h2>
    <a class="more-link" href="#" style="right:15px;top:12px">View all hot villas »</a>
  </div>
  <div class="hot-photo" role="img" aria-label="House with tiled roof"></div>
  <div class="hot-info">
    <h3>2 Bedroom House Rawai Beach</h3>
    <dl>
      <span class="p"><b>Price:</b> THB 3.2M</span><span><b>Type:</b> House/Villa</span>
      <span><b>District:</b> Rawai</span><span><b>Region:</b> South Phuket</span>
    </dl>
  </div>
</section>

<aside class="abs panel badge"><div></div></aside>
</body>
</html>
```